Bref créative
Dormly Nest
HMO Specialists
Professional
Rafik Toumi
Partner
We dont want an adress on the business card
Rafik@dormlynest.co.uk
www.dormlynest.co.uk
I Would like to try with HMO Specialists...O
Or
Letting Agency
Or nothing in the subtitle
The Logo

```html
<!DOCTYPE html>
<html lang="en">
<head>
<meta charset="utf-8">
<title>Dormly Nest — Business Card</title>
<link rel="stylesheet" href="https://fonts.googleapis.com/css2?family=Cinzel:wght@400;600&display=swap">
<style>
  :root {
    --page-bg: #ecebe8;
    --card-bg: #ffffff;
    --brand-green: #3d8b2f;
    --brand-green-dark: #2a6a1f;
    --brand-blue: #3f7fc1;
    --ink: #2b2b2b;
    --ink-soft: #555555;
  }
  * { margin: 0; padding: 0; box-sizing: border-box; }
  html, body {
    width: 1200px;
    height: 804px;
    overflow: hidden;
    background: var(--page-bg);
  }
  .canvas {
    position: relative;
    width: 1200px;
    height: 804px;
  }
  .card {
    position: absolute;
    left: 170px;
    top: 172px;
    width: 860px;
    height: 460px;
    background: var(--card-bg);
    border-radius: 28px;
    box-shadow: 0 6px 18px rgba(0, 0, 0, 0.12);
    overflow: hidden;
    font-family: "Cinzel", serif;
    color: var(--ink);
  }
  .brand {
    position: absolute;
    left: 58px;
    top: 78px;
    display: flex;
    align-items: center;
    gap: 18px;
  }
  .brand-dot {
    width: 40px;
    height: 40px;
    border-radius: 50%;
    background: var(--brand-blue);
  }
  .brand-name {
    font-size: 44px;
    font-weight: 600;
    color: var(--brand-green);
    letter-spacing: 1px;
    line-height: 1;
  }
  .person {
    position: absolute;
    right: 58px;
    top: 50px;
    text-align: right;
  }
  .person-name {
    font-size: 30px;
    font-weight: 600;
    letter-spacing: 0.5px;
  }
  .person-role {
    font-size: 19px;
    margin-top: 4px;
    color: var(--ink);
  }
  .accent-tab {
    position: absolute;
    left: 0;
    top: 240px;
    width: 20px;
    height: 128px;
    border-radius: 0 12px 12px 0;
    background: linear-gradient(90deg, var(--brand-green-dark), var(--brand-green));
  }
  .contacts {
    position: absolute;
    left: 66px;
    top: 244px;
    list-style: none;
  }
  .contacts li {
    display: flex;
    align-items: center;
    gap: 10px;
    height: 31px;
    font-size: 19px;
    color: var(--ink);
  }
  .contacts svg {
    width: 15px;
    height: 15px;
    fill: var(--brand-green);
    flex: none;
  }
</style>
</head>
<body>
<main class="canvas">
  <section class="card">
    <div class="brand">
      <span class="brand-dot"></span>
      <span class="brand-name">Dormly Nest</span>
    </div>

    <div class="person">
      <div class="person-name">Rafik Toumi</div>
      <div class="person-role">Partner</div>
    </div>

    <span class="accent-tab"></span>

    <ul class="contacts">
      <li>
        <svg viewBox="0 0 16 16" aria-hidden="true"><path d="M3.5 1.5l2.5 0 1 3.5-1.8 1.2c.9 1.9 2.3 3.3 4.2 4.2L10.6 8.6l3.5 1v2.5c0 .8-.7 1.5-1.5 1.5C6.8 13.6 2 8.9 2 3c0-.8.7-1.5 1.5-1.5z"/></svg>
        01632 960418
      </li>
      <li>
        <svg viewBox="0 0 16 16" aria-hidden="true"><path d="M5 1h6a1.2 1.2 0 0 1 1.2 1.2v11.6A1.2 1.2 0 0 1 11 15H5a1.2 1.2 0 0 1-1.2-1.2V2.2A1.2 1.2 0 0 1 5 1zm.3 2v8.5h5.4V3zM8 12.3a.8.8 0 1 0 0 1.6.8.8 0 0 0 0-1.6z"/></svg>
        07700 900314
      </li>
      <li>
        <svg viewBox="0 0 16 16" aria-hidden="true"><path d="M1.5 3.5h13v9h-13zm1.4 1.2L8 8.6l5.1-3.9z"/></svg>
        Rafik@dormlynest.co.uk
      </li>
      <li>
        <svg viewBox="0 0 16 16" aria-hidden="true"><path d="M8 1a7 7 0 1 0 0 14A7 7 0 0 0 8 1zm0 1.5c.8 0 1.7 1.6 2 4H6c.3-2.4 1.2-4 2-4zM6 9.5h4c-.3 2.4-1.2 4-2 4s-1.7-1.6-2-4zm-3.4 0h2c.1 1.4.4 2.6.9 3.4a5.5 5.5 0 0 1-2.9-3.4zm0-3a5.5 5.5 0 0 1 2.9-3.4c-.5.8-.8 2-.9 3.4zm8.8 0c-.1-1.4-.4-2.6-.9-3.4a5.5 5.5 0 0 1 2.9 3.4zm0 3h2a5.5 5.5 0 0 1-2.9 3.4c.5-.8.8-2 .9-3.4z"/></svg>
        www.dormlynest.co.uk
      </li>
    </ul>
  </section>
</main>
</body>
</html>
```